Dietitian clinic needs a business card design

We need a business card design for a new dietitian group based in Singapore called "Lantern and Tide". We provide expert, personalised nutrition care to support a wide range of health needs, from chronic conditions to mindful eating. Our team also offers consulting, speaking, and tailored solutions for healthcare providers, organisations, and food services.

Target Market(s)

Adults

Industry/Entity Type

Healthcare

Contact Information for Business Card

Name, position, contact number, email, website address, our logo

Requirements
Nice to have
• Clean, professional but welcoming look

```html
<!DOCTYPE html>
<html lang="en">
<head>
<meta charset="UTF-8">
<title>Lantern and Tide — Business Card</title>
<link href="https://fonts.googleapis.com/css2?family=Playfair+Display:wght@700;800&family=Arimo:wght@400&display=swap" rel="stylesheet">
<style>
  :root {
    --backdrop: #2b2b2c;
    --teal: #265a6b;
    --paper: #ffffff;
    --blush: #e79a9c;
    --ink-light: #ffffff;
  }
  * { margin: 0; padding: 0; box-sizing: border-box; }
  html, body {
    width: 1200px;
    height: 875px;
    overflow: hidden;
    background: var(--backdrop);
  }
  .canvas {
    position: relative;
    width: 1200px;
    height: 875px;
  }
  .card {
    position: absolute;
    top: 286px;
    width: 530px;
    height: 303px;
    border-radius: 22px;
    overflow: hidden;
  }
  .card--front {
    left: 45px;
    background: var(--teal);
    color: var(--ink-light);
  }
  .card--back {
    left: 625px;
    background: var(--paper);
  }
  .card__motif {
    position: absolute;
    inset: 0;
    width: 530px;
    height: 303px;
  }
  .person {
    position: absolute;
    left: 40px;
    top: 128px;
  }
  .person__name {
    font-family: "Playfair Display", Georgia, serif;
    font-weight: 800;
    font-size: 28px;
    line-height: 1.1;
    letter-spacing: 0.2px;
  }
  .person__role {
    font-family: "Arimo", Arial, sans-serif;
    font-size: 14px;
    color: var(--blush);
    margin-top: 2px;
  }
  .contact {
    list-style: none;
    margin-top: 12px;
    font-family: "Arimo", Arial, sans-serif;
    font-size: 13px;
    line-height: 1.35;
  }
  .contact__item {
    display: flex;
    align-items: flex-start;
    gap: 12px;
    margin-bottom: 2px;
  }
  .contact__icon {
    flex: none;
    width: 12px;
    height: 12px;
    margin-top: 3px;
    fill: var(--blush);
  }
  .brand {
    position: absolute;
    right: 52px;
    top: 78px;
    display: flex;
    align-items: flex-start;
    gap: 14px;
    color: var(--teal);
  }
  .brand__dot {
    flex: none;
    width: 30px;
    height: 30px;
    margin-top: 8px;
    border-radius: 50%;
    background: var(--teal);
  }
  .brand__name {
    font-family: "Playfair Display", Georgia, serif;
    font-weight: 800;
    font-size: 40px;
    line-height: 0.95;
    letter-spacing: -0.5px;
  }
</style>
</head>
<body>
<main class="canvas">
  <section class="card card--front" aria-label="Business card front">
    <svg class="card__motif" viewBox="0 0 530 303" aria-hidden="true">
      <circle cx="418" cy="72" r="138" fill="none" stroke="#ffffff" stroke-width="24"/>
    </svg>
    <div class="person">
      <h1 class="person__name">Marcus Lee</h1>
      <p class="person__role">Founder &amp; CEO</p>
      <ul class="contact">
        <li class="contact__item">
          <svg class="contact__icon" viewBox="0 0 16 16" aria-hidden="true"><path d="M8 0a5.5 5.5 0 0 0-5.5 5.5C2.5 10 8 16 8 16s5.5-6 5.5-10.5A5.5 5.5 0 0 0 8 0zm0 7.8a2.3 2.3 0 1 1 0-4.6 2.3 2.3 0 0 1 0 4.6z"/></svg>
          <span>Street Address Here, City<br>State, Country, ZIP 123</span>
        </li>
        <li class="contact__item">
          <svg class="contact__icon" viewBox="0 0 16 16" aria-hidden="true"><path d="M3.6 0.8l2.3 2.9-1.4 1.9c.9 2.2 2.5 3.8 4.7 4.8l1.9-1.4 2.9 2.3-1.2 2.9C7 14 2 9 1.8 2.1z"/></svg>
          <span>(123) 456-7890</span>
        </li>
        <li class="contact__item">
          <svg class="contact__icon" viewBox="0 0 16 16" aria-hidden="true"><path d="M1 3h14v10H1zM2 4.2v.6l6 4.2 6-4.2v-.6z" fill-rule="evenodd"/></svg>
          <span>info@yourwebsitehere.com</span>
        </li>
        <li class="contact__item">
          <svg class="contact__icon" viewBox="0 0 16 16" aria-hidden="true"><circle cx="8" cy="8" r="7"/><path d="M1 8h14M8 1c2.5 2.5 2.5 11.5 0 14M8 1c-2.5 2.5-2.5 11.5 0 14" stroke="#265a6b" stroke-width="1.2" fill="none"/></svg>
          <span>yourwebsitehere.com</span>
        </li>
      </ul>
    </div>
  </section>

  <section class="card card--back" aria-label="Business card back">
    <svg class="card__motif" viewBox="0 0 530 303" aria-hidden="true">
      <circle cx="70" cy="330" r="170" fill="none" stroke="#265a6b" stroke-width="18"/>
    </svg>
    <div class="brand">
      <span class="brand__dot" aria-hidden="true"></span>
      <p class="brand__name">Lantern<br>and Tide</p>
    </div>
  </section>
</main>
</body>
</html>
```